Postcard for friends and family to hint that we are expecting a baby

We are expecting a baby and want to do something a bit special (rather than just announce it on chum wall). We're thinking 'postcard'. Now, this baby is going to be special. Its is a THIRD generation MONKEY (my mother was born in Chinese year of the monkey, as was both my wife and I... and so too will be the baby). We want to make it funny and something that people have to work out - not too difficult, but not blatantly obvious. My wife and I are in our mid (late?) thirties so you can imagine the amount of times we have been asked 'are you going to have kids...' - so with the three generation monkey thing, a couple of clues about a baby being due (ETA 1st Jan-ish) we hope we can create something fun, original and memorable. open to your interpretation.

Target Market(s)

friends and family

Industry/Entity Type

Baby

Font styles to use
Other font styles liked:
• Up to you

Requirements
Must have
• monkeys
• clue(s) that a baby is on the way
• clue(s) about the due date

```html
<!DOCTYPE html>
<html lang="en">
<head>
<meta charset="utf-8">
<title>Baby announcement postcard</title>
<link rel="stylesheet" href="https://fonts.googleapis.com/css2?family=Kurale&display=swap">
<style>
  :root {
    --backdrop: #ecebe8;
    --card: #ffffff;
    --ink: #5a5670;
    --mint: #93d4c2;
    --mint-deep: #5fb59d;
    --mint-pale: #eef8f5;
    --cloud: #bfe5da;
    --stitch: #9a9a9a;
    --rule: #c9c9c9;
    --shadow: rgba(0, 0, 0, 0.22);
  }
  * { box-sizing: border-box; margin: 0; padding: 0; }
  html, body { width: 1200px; height: 800px; overflow: hidden; }
  body {
    background: var(--backdrop);
    font-family: "Kurale", Georgia, serif;
    color: var(--ink);
    position: relative;
  }
  .postcard {
    position: absolute;
    top: 210px;
    width: 560px;
    height: 380px;
    background: var(--card);
    box-shadow: 0 6px 18px var(--shadow);
  }
  .postcard--back { left: 30px; }
  .postcard--front { left: 610px; }
  .postcard svg { display: block; width: 100%; height: 100%; }
  .stitch { fill: none; stroke: var(--stitch); stroke-width: 1.2; stroke-dasharray: 5 4; }
  .stamp-box { fill: none; stroke: var(--rule); stroke-width: 2; }
  .address-line { stroke: var(--rule); stroke-width: 1.5; }
  .cloud-art { fill: var(--cloud); }
  .sign-off { font-family: "Kurale", Georgia, serif; fill: var(--ink); }
  .sign-off__label { font-size: 24px; letter-spacing: 0.5px; }
  .sign-off__names { font-size: 27px; }
  .cloud-pattern { fill: var(--mint-pale); }
  .ribbon-band { fill: var(--mint); }
  .ribbon-band__stripe { stroke: #a9ddd0; stroke-width: 2; }
  .frame-scallop { fill: var(--cloud); }
  .frame-inner { fill: #f6fbfa; }
  .frame-stitch { fill: none; stroke: #7d8a88; stroke-width: 1; stroke-dasharray: 4 3; }
  .due-date { font-family: "Kurale", Georgia, serif; font-size: 17px; fill: var(--mint-deep); }
  .banner-tail { fill: var(--mint); }
  .banner-face { fill: #ffffff; stroke: var(--mint); stroke-width: 4; }
  .banner-text { font-family: "Kurale", Georgia, serif; font-size: 21px; fill: var(--ink); }
</style>
</head>
<body>

<section class="postcard postcard--back" aria-label="Postcard back">
  <svg viewBox="0 0 560 380">
    <defs>
      <linearGradient id="cloudTone" x1="0" y1="0" x2="1" y2="0">
        <stop offset="0" stop-color="#b5e2d6"/>
        <stop offset="1" stop-color="#c8ebe1"/>
      </linearGradient>
    </defs>
    <rect class="stitch" x="14" y="14" width="532" height="352"/>
    <rect class="stamp-box" x="455" y="32" width="72" height="52"/>
    <line class="address-line" x1="330" y1="170" x2="520" y2="170"/>
    <line class="address-line" x1="330" y1="205" x2="520" y2="205"/>
    <line class="address-line" x1="330" y1="240" x2="520" y2="240"/>
    <line class="address-line" x1="330" y1="275" x2="520" y2="275"/>
    <rect class="cloud-art" role="img" aria-label="Two soft mint clouds" x="40" y="48" width="150" height="70" rx="30" fill="url(#cloudTone)"/>
    <text class="sign-off sign-off__label" x="60" y="185">LOVE FROM</text>
    <text class="sign-off sign-off__names" x="60" y="222">Rowan and Maribel</text>
  </svg>
</section>

<section class="postcard postcard--front" aria-label="Postcard front">
  <svg viewBox="0 0 560 380">
    <defs>
      <linearGradient id="monkeyTone" x1="0" y1="0" x2="0" y2="1">
        <stop offset="0" stop-color="#a88a6a"/>
        <stop offset="1" stop-color="#c9ad8e"/>
      </linearGradient>
      <linearGradient id="balloonTone" x1="0" y1="0" x2="1" y2="1">
        <stop offset="0" stop-color="#f7d774"/>
        <stop offset="0.35" stop-color="#8fd3c1"/>
        <stop offset="0.65" stop-color="#a9a9b0"/>
        <stop offset="1" stop-color="#f0952e"/>
      </linearGradient>
    </defs>
    <rect class="cloud-pattern" role="img" aria-label="Pale mint cloud pattern background" x="0" y="0" width="560" height="380"/>
    <rect class="stitch" x="12" y="12" width="536" height="356"/>

    <g class="ribbon-band">
      <rect x="0" y="170" width="560" height="62"/>
      <g class="ribbon-band__stripe">
        <line x1="0" y1="180" x2="560" y2="180"/>
        <line x1="0" y1="222" x2="560" y2="222"/>
      </g>
    </g>

    <ellipse class="frame-scallop" cx="250" cy="228" rx="104" ry="134"/>
    <ellipse class="frame-inner" cx="250" cy="228" rx="92" ry="122"/>
    <ellipse class="frame-stitch" cx="250" cy="228" rx="84" ry="114"/>

    <text class="due-date" x="118" y="100" transform="rotate(-22 118 100)">ETA 1st Jan-ish</text>

    <rect role="img" aria-label="Bunch of polka-dot balloons in yellow, mint, grey, orange and lilac" x="262" y="30" width="200" height="150" rx="60" fill="url(#balloonTone)"/>
    <rect role="img" aria-label="Cartoon baby monkey holding the balloon strings" x="185" y="190" width="140" height="150" rx="40" fill="url(#monkeyTone)"/>

    <polygon class="banner-tail" points="140,318 175,318 175,356 140,356 152,337"/>
    <polygon class="banner-tail" points="425,306 460,306 448,325 460,344 425,344"/>
    <polygon class="banner-face" points="165,320 435,308 435,345 165,358"/>
    <text class="banner-text" x="300" y="342" text-anchor="middle" transform="rotate(-2.5 300 338)">We are Expecting a Baby!</text>
  </svg>
</section>

</body>
</html>
```